Plakat-Design für Vereinsfest
Zielgruppe
Unser Verein veranstaltet jedes Jahr im August das Vereinsfest 'Sonnwendtag', das in einem kleinen Wäldchen innerhalb des Heimatortes stattfindet. Am Samstag und Sonntag sorgen verschiedene Musikgruppen für Unterhaltung. Es soll ein Veranstaltungsplakat gestaltet werden, dass sich an die Vorgaben (siehe unten) hält und die Veranstaltung bewirbt.
Zielgruppe sind Bürger des Heimatortes.
Aufgabenstellung
Das Vereinslogo ist beigefügt und sollte prominent auf dem Plakat vertreten sein, Logo und Schriftzug können auch getrennt oder anders angeordnet werden. Der Veranstaltungstitel lautet "Sonnwendtag", es findet am 20. und 21. August "Am Hirtenstein" (Veranstaltungsort) statt.
Programmpunkte: Samstag: Musikalische Unterhaltung mit den Bachpfeifern; Sonntag: Musikalische Unterhaltung mit den Moorbachrabauken
Uhrzeiten sollten enthalten sein:
Beginn Samstag: ab 15 Uhr
Beginn Sonntag: ab 10 Uhr
Das Plakat soll gut leserlich auch aus der Entfernung sein, da es an Straßen plakatiert wird.
Das Plakat soll für spätere Jahre editierbar sein.
Schriftart im Logo: Californian FB Bold (muss aber nicht auf andere Textelemente angewendet werden). Das Plakat soll in DIN A2 gedruckt werden. Die Webadresse sollte auf dem Plakat stehen.

```html
<!DOCTYPE html>
<html lang="de">
<head>
<meta charset="utf-8">
<title>Sonnwendtag – Plakat</title>
<link href="https://fonts.googleapis.com/css2?family=Abril+Fatface&family=Source+Serif+4:opsz,wght@8..60,600;8..60,700&display=swap" rel="stylesheet">
<style>
  :root {
    --blue: #185a8a;
    --blue-soft: #c9d8e6;
    --paper: #f4f3f1;
    --backdrop: #e6e6e4;
    --ink: #3a3a3a;
    --slate: #4f4f4f;
    --white: #ffffff;
    --grey-soft: #cfcfcf;
  }
  * { margin: 0; padding: 0; box-sizing: border-box; }
  html, body { width: 1200px; height: 1178px; overflow: hidden; background: var(--backdrop); }
  .poster {
    position: absolute; left: 197px; top: 19px; width: 806px; height: 1140px;
    background: var(--paper);
    font-family: "Source Serif 4", Georgia, serif;
    text-align: center;
  }
  .frame-outer, .frame-inner { position: absolute; border: 3px solid var(--blue); }
  .frame-outer { inset: 14px; }
  .frame-inner { inset: 22px; border-width: 1.5px; }
  .ornament { position: absolute; width: 120px; height: 120px; background: var(--blue-soft); opacity: .55; }
  .ornament.tl { left: 32px; top: 32px; border-radius: 0 0 100% 0; }
  .ornament.tr { right: 32px; top: 32px; border-radius: 0 0 0 100%; }
  .ornament.bl { left: 32px; bottom: 32px; border-radius: 0 100% 0 0; }
  .ornament.br { right: 32px; bottom: 32px; border-radius: 100% 0 0 0; }

  .club { position: absolute; top: 78px; left: 0; right: 0; display: flex; justify-content: center; align-items: center; gap: 22px; }
  .club-mark { width: 108px; height: 108px; border-radius: 50%; background: var(--blue-soft); flex: none; }
  .club-name { color: var(--blue); font-weight: 600; font-size: 27px; line-height: 1.05; text-align: left; }

  .title {
    position: absolute; top: 262px; left: 0; right: 0;
    font-family: "Abril Fatface", "Bodoni Moda", serif;
    color: var(--blue); font-size: 82px; letter-spacing: -1px; line-height: 1;
    transform: scaleY(1.45); transform-origin: top center;
  }
  .date-band {
    position: absolute; top: 452px; left: 52px; right: 52px; height: 112px;
    background: var(--blue); color: var(--white);
    padding-top: 8px;
  }
  .date-band .dates { font-weight: 700; font-size: 50px; line-height: 1.1; }
  .date-band .venue { font-weight: 600; font-size: 32px; line-height: 1.15; }

  .program { position: absolute; top: 600px; left: 60px; right: 60px; display: flex; justify-content: space-between; }
  .day { width: 48%; }
  .day h2 { color: var(--ink); font-weight: 700; font-size: 29px; letter-spacing: .5px; margin-bottom: 4px; }
  .day p { color: var(--blue); font-weight: 700; font-size: 23px; line-height: 1.3; }

  .times {
    position: absolute; top: 792px; left: 50%; transform: translateX(-50%);
    background: var(--slate); color: var(--white);
    font-weight: 600; font-size: 27px; line-height: 1.2;
    padding: 14px 34px; white-space: nowrap;
  }
  .headwear { position: absolute; top: 900px; left: 210px; right: 210px; display: flex; justify-content: space-between; align-items: flex-end; height: 170px; }
  .headwear div { background: linear-gradient(#6b6b6b, var(--grey-soft)); border-radius: 40% 40% 8px 8px; }
  .hat-plume { width: 100px; height: 160px; }
  .hat-crown { width: 140px; height: 120px; background: linear-gradient(#d8d8d8, #eeeeee) !important; }
  .hat-shako { width: 100px; height: 165px; }

  .web { position: absolute; bottom: 40px; left: 0; right: 0; color: var(--ink); font-weight: 700; font-size: 26px; }
</style>
</head>
<body>
  <main class="poster">
    <div class="frame-outer"></div>
    <div class="frame-inner"></div>
    <div class="ornament tl" role="img" aria-label="Eckornament"></div>
    <div class="ornament tr" role="img" aria-label="Eckornament"></div>
    <div class="ornament bl" role="img" aria-label="Eckornament"></div>
    <div class="ornament br" role="img" aria-label="Eckornament"></div>

    <header class="club">
      <span class="club-mark"></span>
      <p class="club-name">Historischer Schützenzug<br>und Heimatgruppe<br>Talbrunn e.V.</p>
    </header>

    <h1 class="title">SONNWENDTAG</h1>

    <section class="date-band">
      <p class="dates">20. - 21. August</p>
      <p class="venue">“Am Hirtenstein”</p>
    </section>

    <section class="program">
      <article class="day">
        <h2>SAMSTAG:</h2>
        <p>Musikalische<br>Unterhaltung mit den<br>Bachpfeifern</p>
      </article>
      <article class="day">
        <h2>SONNTAG:</h2>
        <p>Musikalische<br>Unterhaltung mit den<br>Moorbachrabauken</p>
      </article>
    </section>

    <p class="times">Beginn Samstag: ab 15 Uhr<br>Beginn Sonntag: ab 10 Uhr</p>

    <div class="headwear">
      <div class="hat-plume" role="img" aria-label="Illustration eines Helms mit Federbusch"></div>
      <div class="hat-crown" role="img" aria-label="Illustration einer Trachtenhaube"></div>
      <div class="hat-shako" role="img" aria-label="Illustration eines Tschakos"></div>
    </div>

    <p class="web">www.schuetzenzug-talbrunn.de</p>
  </main>
</body>
</html>
```